Stellenanzeige / Anzeigengestaltung für Haustechnikbetrieb
Zielgruppe
Wir sind ein Haustechnikbetrieb. Unsere Schwerpunkte liegen im Bereich Heizungs- Sanitär- u. Klimatechnik, sowie Elektroinstallation für Ein- u. Zweifamilienhäuser.
Ich möchte eine kreative Stellenanzeige, die unsere Vorteile gegenüber den Bewerberfirmen herausstellt.
Aufgabenstellung
Anzeigenschaltung in Printmedien und sozialen Netzwerken
für die Onlineanzeige:
Werbebanner Größe 240x400 Pixel
Bezeichnung(en): Vertical Rectangle, Fat Skyscraper, Vertikales Rechteck
Fläche in Pixel: 96.000
Für Print:
1/4 Seite HOCH 8,4 x 12,6 cm
mögliche Texte:
LUST auf was NEUES? JA!
Das trifft sich gut!
ANLAGENMECHANIKER SHK (M/W) gesucht
o Heimatnaher Arbeitseinsatz oder näheres Umfeld
o 70,00 € Auslöse (bei Übernachung)
o Pünktliche, überdurchschnittliche Bezahlung
o Alle Fahrtstunden werden voll bezahlt
o Dienstwagen
o moderne Werkzeuge, Arbeits- und mobile Endgeräte
o Weihnachtsgeld
o Tankgutscheine
o Zulagen für Hochzeit, Jubiläum (...)
o Weiterbildungsmnaßnahmen und Schulungen
o und vieles mehr...
Alles Weitere erfährst du im persönlichen Gespräch.

```html
<!DOCTYPE html>
<html lang="de">
<head>
<meta charset="utf-8">
<title>Stellenanzeige Anlagenmechaniker SHK</title>
<link rel="stylesheet" href="https://fonts.googleapis.com/css2?family=Roboto+Condensed:ital,wght@0,300;0,400;0,700;1,400&display=swap">
<style>
  :root {
    --page-bg: #e6e6e6;
    --card-bg: #ffffff;
    --orange: #e8781a;
    --navy: #2a1f6b;
    --ink: #1c1c1c;
    --photo-light: #efebe6;
    --photo-mid: #d9cfc3;
    --photo-dark: #b9a894;
  }
  * { margin: 0; padding: 0; box-sizing: border-box; }
  html, body {
    width: 1200px; height: 1200px; overflow: hidden;
    background: var(--page-bg);
    font-family: "Roboto Condensed", sans-serif;
  }
  .ad {
    position: absolute; left: 213px; top: 20px;
    width: 774px; height: 1160px;
    background: var(--card-bg);
    overflow: hidden;
  }
  .hero {
    position: absolute; left: 0; top: 0; width: 100%; height: 364px;
    background: linear-gradient(180deg, var(--photo-light) 0%, #e8e2db 45%, var(--photo-mid) 75%, var(--photo-dark) 100%);
  }
  .hero-band {
    position: absolute; left: 0; top: 364px; width: 100%; height: 14px;
    background: var(--orange);
  }
  .headline {
    position: absolute; left: 46px; top: 38px;
    font-weight: 700; font-size: 64px; line-height: 66px;
    color: var(--orange); letter-spacing: -0.5px;
  }
  .corner-mark { position: absolute; left: 644px; top: 45px; }
  .job-title {
    position: absolute; left: 46px; top: 408px;
    font-weight: 700; font-size: 58px; line-height: 62px;
    color: var(--navy); letter-spacing: -0.5px;
  }
  .benefits {
    position: absolute; left: 64px; top: 540px;
    list-style: none;
    font-weight: 400; font-size: 30px; line-height: 34.2px;
    color: var(--ink);
  }
  .benefits li { position: relative; padding-left: 35px; }
  .benefits li::before {
    content: ""; position: absolute; left: 0; top: 8px;
    width: 14px; height: 14px; background: var(--navy);
  }
  .closing {
    position: absolute; left: 46px; top: 934px;
    font-style: italic; font-size: 29px; line-height: 35px;
    color: var(--ink);
  }
  .closing p + p { margin-top: 14px; }
  .closing .email { font-style: normal; font-weight: 700; color: var(--navy); }
  .brand-frame { position: absolute; left: 516px; top: 905px; width: 210px; height: 210px; }
  .brand-name {
    position: absolute; left: 516px; top: 905px; width: 210px; height: 210px;
    display: flex; align-items: center; justify-content: center;
    font-weight: 700; font-size: 52px; color: var(--navy); letter-spacing: 1px;
  }
</style>
</head>
<body>
  <div class="ad">
    <div class="hero" role="img" aria-label="Foto: zwei Handwerker auf Holzleitern arbeiten an einer Deckenöffnung in einem hellen Raum"></div>
    <div class="hero-band"></div>
    <h1 class="headline">Lust auf neue<br>Perspektiven?</h1>
    <svg class="corner-mark" width="83" height="83" viewBox="0 0 83 83" aria-hidden="true">
      <path d="M0 0 H83 V83 H65 V18 H0 Z" fill="var(--navy)"/>
    </svg>

    <h2 class="job-title">ANLAGENMECHANIKER SHK<br>(M/W) gesucht</h2>

    <ul class="benefits">
      <li>Heimatnaher Arbeitseinsatz oder näheres Umfeld</li>
      <li>70,00 € Auslöse (bei Übernachung)</li>
      <li>Pünktliche, überdurchschnittliche Bezahlung</li>
      <li>Alle Fahrtstunden werden voll bezahlt</li>
      <li>Dienstwagen</li>
      <li>Moderne Werkzeuge, Arbeits- und mobile Endgeräte</li>
      <li>Weihnachtsgeld</li>
      <li>Tankgutscheine</li>
      <li>Zulagen für Hochzeit, Jubiläum (...)</li>
      <li>Weiterbildungsmnaßnahmen und Schulungen</li>
      <li>und vieles mehr ...</li>
    </ul>

    <div class="closing">
      <p>Alles Weitere erfährst Du im<br>persönlichen Gespräch.</p>
      <p>Wir freuen uns auf Deine Bewerbung<br>per E-Mail an Tobias Grünfeld,<br><span class="email">tobias.grunfeld@kalver-gmbh.de.</span></p>
    </div>

    <svg class="brand-frame" viewBox="0 0 210 210" aria-hidden="true">
      <g fill="var(--navy)">
        <path d="M0 0 H32 V7 H7 V32 H0 Z"/>
        <path d="M210 0 H178 V7 H203 V32 H210 Z"/>
        <path d="M0 210 H32 V203 H7 V178 H0 Z"/>
      </g>
    </svg>
    <div class="brand-name">KALVER</div>
  </div>
</body>
</html>
```